Marcus Delvane Wellness podcast

I have overcome many health challenges. All of them have put me in position to help other people do the same. Eventually I became a certified health coach through the Academy of Restorative Dietetics. I have a strong desire to help because I know what it’s like to not feel well, and do what you want. The content on this sight will equip you with the tools to live a life full of health, freedom, and happiness. Complex health topics are broken down into simple ways to understand. No wellness topic is off limits, whether its heart disease, cancer, diabetes, sleep, hormones, or any other wellness topic.

Target Market(s)

People who are interested in growth and getting healthier

Industry/Entity Type

Health and Wellness

Colors
0054AA
0677BA
7BADD7
CADEEF
E8F1F8
0094D4
00A9DD
6FCCEA
C7EBF8
E9F6FB

Requirements
Must have
• None
Nice to have
• None
Should not have
• None

```html
<!DOCTYPE html>
<html lang="en">
<head>
<meta charset="UTF-8">
<title>Marcus Delvane Wellness Podcast</title>
<link rel="stylesheet" href="https://fonts.googleapis.com/css2?family=Montserrat:ital,wght@1,400;1,500;1,800;1,900&display=swap">
<style>
  :root {
    --blue-deep: #0a3fd9;
    --blue-mid: #0677ba;
    --blue-bright: #0094d4;
    --green: #00c853;
    --green-bright: #22f04a;
    --teal: #00a9dd;
    --white: #ffffff;
    --shirt: #c7ebf8;
    --mic-pink: #d77bd0;
    --mic-violet: #8a63c9;
  }
  * { margin: 0; padding: 0; box-sizing: border-box; }
  html, body { width: 1200px; height: 1200px; overflow: hidden; }
  body { font-family: 'Montserrat', sans-serif; }
  .cover {
    position: relative;
    width: 1200px;
    height: 1200px;
    overflow: hidden;
    background: linear-gradient(160deg, var(--blue-mid) 0%, var(--blue-bright) 35%, #0b5fe0 70%, var(--blue-deep) 100%);
  }
  .backdrop { position: absolute; inset: 0; width: 1200px; height: 1200px; }
  .host-photo {
    position: absolute;
    left: 0;
    top: 84px;
    width: 590px;
    height: 1116px;
    border-radius: 260px 260px 0 0;
    background: linear-gradient(180deg, #9fd6e8 0%, var(--shirt) 35%, #8fe3ef 70%, #3fb8e0 100%);
  }
  .headline {
    position: absolute;
    left: 560px;
    top: 298px;
    width: 610px;
    text-align: center;
    color: var(--white);
    font-style: italic;
    text-transform: uppercase;
    font-size: 48px;
    line-height: 51px;
    letter-spacing: 0.5px;
  }
  .headline .light { font-weight: 400; display: block; }
  .headline .strong { font-weight: 900; display: block; }
  .byline {
    position: absolute;
    left: 684px;
    top: 752px;
    color: var(--white);
    font-style: italic;
    text-transform: uppercase;
    font-size: 41px;
    line-height: 46px;
  }
  .byline .by { font-weight: 500; }
  .byline .name { font-weight: 900; }
  .byline .second { display: block; padding-left: 12px; }
  .mic-art {
    position: absolute;
    left: 960px;
    top: 702px;
    width: 230px;
    height: 498px;
    border-radius: 110px 110px 20px 20px;
    background: linear-gradient(180deg, var(--mic-pink) 0%, var(--mic-violet) 45%, #5a7fd8 100%);
  }
</style>
</head>
<body>
<main class="cover">
  <svg class="backdrop" viewBox="0 0 1200 1200" aria-hidden="true">
    <defs>
      <linearGradient id="big-circle-fill" x1="0" y1="0" x2="0" y2="1">
        <stop offset="0" stop-color="#00c853"/>
        <stop offset="0.55" stop-color="#02b889"/>
        <stop offset="1" stop-color="#0094d4" stop-opacity="0.4"/>
      </linearGradient>
      <linearGradient id="small-circle-fill" x1="0" y1="0" x2="0" y2="1">
        <stop offset="0" stop-color="#22f04a"/>
        <stop offset="0.6" stop-color="#10d873"/>
        <stop offset="1" stop-color="#00a9dd" stop-opacity="0.3"/>
      </linearGradient>
      <linearGradient id="bar-fill" x1="0" y1="0" x2="0" y2="1">
        <stop offset="0" stop-color="#6fccea" stop-opacity="0.5"/>
        <stop offset="1" stop-color="#6fccea" stop-opacity="0"/>
      </linearGradient>
    </defs>
    <circle class="halo-large" cx="920" cy="390" r="520" fill="url(#big-circle-fill)"/>
    <circle class="halo-small" cx="200" cy="520" r="310" fill="url(#small-circle-fill)"/>
    <g class="plus-marks" fill="none" stroke-width="8" stroke-linejoin="round">
      <path stroke="#0677ba" stroke-opacity="0.55" d="M88 74h38v38h38v38h-38v38H88v-38H50v-38h38z"/>
      <path stroke="#7bf0a8" stroke-opacity="0.6" d="M1008 84h46v50h48v46h-48v50h-46v-50h-50v-46h50z"/>
      <path stroke="#0677ba" stroke-opacity="0.5" d="M530 456h40v40h40v40h-40v40h-40v-40h-40v-40h40z"/>
    </g>
    <g class="level-bars" fill="url(#bar-fill)">
      <rect x="622" y="1060" width="16" height="140" rx="8"/>
      <rect x="658" y="1010" width="16" height="190" rx="8"/>
      <rect x="694" y="978" width="16" height="222" rx="8"/>
      <rect x="730" y="1040" width="16" height="160" rx="8"/>
      <rect x="766" y="1000" width="16" height="200" rx="8"/>
      <rect x="802" y="1070" width="16" height="130" rx="8"/>
      <rect x="838" y="990" width="16" height="210" rx="8"/>
      <rect x="874" y="954" width="16" height="246" rx="8"/>
      <rect x="910" y="1030" width="16" height="170" rx="8"/>
      <rect x="946" y="1010" width="16" height="190" rx="8"/>
    </g>
  </svg>

  <div class="host-photo" role="img" aria-label="Portrait photo of the podcast host smiling, wearing a light blue t-shirt"></div>

  <h1 class="headline">
    <span class="light">Equip yourself</span>
    <span class="light">with the toos</span>
    <span class="light">to live a life full</span>
    <span class="strong">of health,</span>
    <span class="strong">freedom,</span>
    <span class="strong">and happiness</span>
  </h1>

  <p class="byline"><span class="by">By </span><span class="name">Marcus</span><span class="name second">Delvane</span></p>

  <div class="mic-art" role="img" aria-label="Illustration of a pink retro studio microphone on a stand"></div>
</main>
</body>
</html>
```